Book title: Lanternfall: The spark of momentum!

This book is called: Lanternfall: The spark of momentum!

A guide to understanding the most popular types of coaching and how to find the perfect coach for you.
The coaching industry has exploded over the past few years as the demand for them has increased. With so many different types of coaches it can be intimidating and overwhelming to find the perfect one for you. To further complicate matters, you may experience times in your life when you require multiple coaches. {Book Title} aims to quite the noise and assist you in finding the perfect coach for you. In this book, you will learn more about the different types of coaching as well as meet a hand-picked selection of coaches from the most popular coaching niches. Each featured coach has provided an exercise designed to move you powerfully forward. We encourage you to work through each exercise so you may experience firsthand the power of working with these incredible coaches.

We would like a professional and simple design. See examples included. We would like to see blood orange included in the design, please see color pallets included as well.

Target Market(s)

Corporate professionals wanting to explore the various types of coaching industry

Industry/Entity Type

Coaching - Health, business, spiritual

Font styles to use
Serif

Colors
EE7325
F08F49
F5BC92
FAE3D3
FDF4ED

Requirements
Must have
• Please include book title: Lanternfall, Subtitle: The spark of momentum! Name of publishing company: Silver Meadow Publishing, Spaces for 8 author names on the front of the cover- Author Name
Nice to have
• A feminine yet corporate feel.
Should not have
• We don't want it

```html
<!DOCTYPE html>
<html lang="en">
<head>
<meta charset="utf-8">
<title>Lanternfall: The spark of momentum!</title>
<link rel="stylesheet" href="https://fonts.googleapis.com/css2?family=Anton&family=Cinzel:wght@400;700;900&display=swap">
<style>
  :root {
    --sky-deep: #03428a;
    --sky-mid: #1f5fa3;
    --cloud: #a9b8c6;
    --peach-mist: #f5bc92;
    --orange-soft: #f08f49;
    --blood-orange: #ee7325;
    --peach-pale: #fae3d3;
    --cream: #fdf4ed;
    --horizon: #8a4418;
    --sand-dark: #1c120b;
    --sand-black: #0b0805;
    --title-ink: #161526;
    --outline: #ffffff;
    --author: #ffffff;
  }
  * { margin: 0; padding: 0; box-sizing: border-box; }
  html, body { width: 848px; height: 1200px; overflow: hidden; background: #ffffff; }
  .cover { position: relative; width: 848px; height: 1200px; overflow: hidden; }
  .cover-photo {
    position: absolute; inset: 0;
    background:
      radial-gradient(ellipse 110px 90px at 460px 740px, var(--cream) 0%, rgba(253,244,237,0.65) 40%, rgba(240,143,73,0) 100%),
      linear-gradient(180deg,
        var(--sky-deep) 0%,
        var(--sky-deep) 28%,
        var(--sky-mid) 40%,
        var(--cloud) 50%,
        var(--peach-mist) 56%,
        var(--orange-soft) 62%,
        var(--blood-orange) 68%,
        var(--horizon) 74%,
        #3d2412 80%,
        var(--sand-dark) 87%,
        var(--sand-black) 100%);
  }
  .title-block { position: absolute; left: 0; top: 0; width: 848px; height: 360px; }
  .title-main {
    font-family: "Anton", "Impact", sans-serif;
    font-size: 150px;
    fill: var(--title-ink);
    stroke: var(--outline);
    stroke-width: 10px;
    paint-order: stroke;
    stroke-linejoin: round;
  }
  .title-sub {
    font-family: "Cinzel", "Times New Roman", serif;
    font-weight: 900;
    font-size: 62px;
    fill: #0c0c12;
    stroke: var(--outline);
    stroke-width: 6px;
    paint-order: stroke;
    stroke-linejoin: round;
  }
  .author-list {
    position: absolute; left: 64px; top: 958px; width: 720px;
    display: grid; grid-template-columns: 1fr 1fr; row-gap: 18px; column-gap: 40px;
    list-style: none;
  }
  .author-name {
    font-family: "Cinzel", "Times New Roman", serif;
    font-weight: 400;
    font-size: 22px;
    line-height: 26px;
    letter-spacing: 0.36em;
    color: var(--author);
    text-align: center;
    white-space: nowrap;
  }
  .publisher {
    position: absolute; left: 0; top: 1146px; width: 848px;
    font-family: "Cinzel", "Times New Roman", serif;
    font-weight: 700;
    font-size: 16px;
    letter-spacing: 0.3em;
    color: var(--orange-soft);
    text-align: center;
  }
</style>
</head>
<body>
  <main class="cover">
    <div class="cover-photo" role="img" aria-label="Five people silhouetted jumping with raised arms on a beach at sunset, under a blue sky with streaked clouds and an orange glow"></div>

    <svg class="title-block" width="848" height="360" viewBox="0 0 848 360" aria-label="Lanternfall: The spark of momentum!">
      <text class="title-main" x="73" y="185" textLength="713" lengthAdjust="spacingAndGlyphs">LANTERNFALL</text>
      <text class="title-sub" x="167" y="272" textLength="502" lengthAdjust="spacingAndGlyphs">THE SPARK OF</text>
      <text class="title-sub" x="240" y="329" textLength="372" lengthAdjust="spacingAndGlyphs">MOMENTUM!</text>
    </svg>

    <ul class="author-list">
      <li class="author-name">AUTHOR NAME</li>
      <li class="author-name">AUTHOR NAME</li>
      <li class="author-name">AUTHOR NAME</li>
      <li class="author-name">AUTHOR NAME</li>
      <li class="author-name">AUTHOR NAME</li>
      <li class="author-name">AUTHOR NAME</li>
      <li class="author-name">AUTHOR NAME</li>
      <li class="author-name">AUTHOR NAME</li>
    </ul>

    <p class="publisher">SILVER MEADOW PUBLISHING</p>
  </main>
</body>
</html>
```